Bramblegate Card Company Business Cards

We are a trading card store with Zorvanix, sports and other TCG cards, we need a business card design that encompasses a clean cut, modern style with a retro flare. website is bramblegatecardco.example for reference. Can utilize a comic book era feel or a more modern outdoor feel to utilize the "Pacific Northwest" elements of tress, mountains, etc.

Industry/Entity Type

Trading cards and collectibles

Contact Information for Business Card

business name, email address, phone number, name, owner job title

Font styles to use
Sans Serif

```html
<!DOCTYPE html>
<html lang="en">
<head>
<meta charset="utf-8">
<title>Bramblegate Card Company – Business Cards</title>
<link rel="stylesheet" href="https://fonts.googleapis.com/css2?family=Montserrat:wght@400;500;700;800&display=swap">
<style>
  :root {
    --stage: #232323;
    --paper: #ffffff;
    --cyan: #22bfe0;
    --slate: #6b6b6b;
    --ink: #2f2f2f;
    --rule: #9a9a9a;
    --back-top: #8a8a8a;
    --back-bottom: #5f5f5f;
  }
  * { box-sizing: border-box; margin: 0; padding: 0; }
  html, body {
    width: 1200px; height: 801px; overflow: hidden;
    background: var(--stage);
    font-family: "Montserrat", sans-serif;
  }
  .sheet {
    position: relative; width: 1200px; height: 801px;
    display: flex; align-items: center; justify-content: center; gap: 40px;
  }
  .card {
    position: relative; width: 540px; height: 309px;
    border-radius: 18px; overflow: hidden;
  }
  .card-front { background: var(--paper); }
  .front-band { position: absolute; inset: 0; width: 100%; height: 100%; }
  .brand-mark {
    position: absolute; left: 40px; top: 98px; width: 180px;
    display: flex; align-items: center; gap: 10px;
  }
  .brand-dot {
    flex: none; width: 16px; height: 16px; border-radius: 50%;
    background: var(--cyan);
  }
  .brand-name {
    font-weight: 800; font-size: 19px; line-height: 1.15;
    color: var(--slate); text-transform: uppercase; letter-spacing: 0.5px;
  }
  .divider {
    position: absolute; left: 238px; top: 70px; width: 1px; height: 140px;
    background: var(--rule);
  }
  .contact {
    position: absolute; left: 262px; top: 52px;
    color: var(--ink); font-size: 12.5px; line-height: 1.45;
  }
  .contact-name {
    font-weight: 800; font-size: 21px; color: var(--cyan);
    letter-spacing: 0.5px; text-transform: uppercase; line-height: 1.1;
  }
  .contact-title { font-size: 12.5px; margin-bottom: 10px; }
  .contact-address { margin-bottom: 10px; }
  .contact-line { display: flex; align-items: center; gap: 7px; }
  .contact-line svg { width: 11px; height: 11px; flex: none; }

  .card-back {
    background: linear-gradient(160deg, var(--back-top), var(--back-bottom));
    display: flex; align-items: center; justify-content: center;
  }
  .back-mark {
    display: flex; align-items: center; gap: 14px;
  }
  .back-mark .brand-dot { width: 22px; height: 22px; }
  .back-mark .brand-name {
    color: var(--paper); font-size: 26px;
  }
</style>
</head>
<body>
<main class="sheet">
  <section class="card card-front" aria-label="Business card front">
    <svg class="front-band" viewBox="0 0 540 309" preserveAspectRatio="none" aria-hidden="true">
      <path d="M540 110 C470 200 300 270 110 309 L540 309 Z" fill="var(--cyan)"/>
      <path d="M510 118 C430 210 280 270 110 300" fill="none" stroke="var(--slate)" stroke-width="2"/>
    </svg>
    <div class="brand-mark">
      <span class="brand-dot"></span>
      <span class="brand-name">Bramblegate Card Company</span>
    </div>
    <div class="divider"></div>
    <div class="contact">
      <p class="contact-name">Dorian Vale</p>
      <p class="contact-title">CEO/Founder</p>
      <p class="contact-address">P.O. Box 3178 Street<br>Country Name AB 6021</p>
      <p class="contact-line">
        <svg viewBox="0 0 12 12"><path d="M2 1 L4.5 1 L5.5 3.5 L4 4.5 C4.8 6.3 5.7 7.2 7.5 8 L8.5 6.5 L11 7.5 L11 10 C6 11 1 6 2 1 Z" fill="var(--cyan)"/></svg>
        (555) 014 2290
      </p>
      <p class="contact-line">
        <svg viewBox="0 0 12 12"><rect x="1" y="2.5" width="10" height="7" fill="var(--cyan)"/><path d="M1 2.5 L6 6.5 L11 2.5" fill="none" stroke="#fff" stroke-width="1"/></svg>
        info@bramblegatecardco.example
      </p>
      <p class="contact-line">
        <svg viewBox="0 0 12 12"><circle cx="6" cy="6" r="5" fill="var(--cyan)"/><path d="M1 6 H11 M6 1 C3.5 4 3.5 8 6 11 M6 1 C8.5 4 8.5 8 6 11" fill="none" stroke="#fff" stroke-width="0.8"/></svg>
        www.bramblegatecardco.example
      </p>
    </div>
  </section>

  <section class="card card-back" aria-label="Business card back">
    <div class="back-mark">
      <span class="brand-dot"></span>
      <span class="brand-name">Bramblegate<br>Card Company</span>
    </div>
  </section>
</main>
</body>
</html>
```